Luxury Face Oil Label

I'm looking for a simple and sophisticated design for a natural face oil that will target the luxe market. It is a pure Natural product. I have attached the logo, Velmora Organics.

Here's the Copy

LUXE FACIAL OIL

Regenerate. Hydrate. Glow

100% Natural

30ml (1.01 oz)

A complex blend of Pure Oils including Marula, Sea Buckthorn, Rosehip, Neroli, Evening primrose, Argan, Calendula, Lavender, Jojoba, Grapeseed, Baobab, Moringa and Vitamin E oil.

Produced by
Copper Lantern Ltd
P.O box 7825-00300
Nairobi, Kenya
www.velmoraorganics.example

Target Market(s)

High end

Requirements
Must have
• Simple, Please consider the bottle, which is a 30ml clear glass bottle with a gold and white pump. Image attached.
Nice to have
• Very clean designs, not too much going on.
Should not have
• Leaves and nuts.

```html
<!DOCTYPE html>
<html lang="en">
<head>
<meta charset="utf-8">
<title>Solvanta Luxe Facial Oil Label</title>
<link rel="stylesheet" href="https://fonts.googleapis.com/css2?family=Roboto:wght@300;400&family=Allura&display=swap">
<style>
  :root {
    --page: #ffffff;
    --ink: #2e2e30;
    --ink-soft: #6a6a6c;
    --copper: #b07a44;
    --dieline: #e0403c;
    --gold-light: #f6dfae;
    --gold-mid: #e9b664;
    --gold-deep: #c6782f;
    --marble-white: #ffffff;
    --marble-gold: #efe1c2;
  }
  html, body {
    margin: 0;
    padding: 0;
    width: 720px;
    height: 1200px;
    overflow: hidden;
    background: var(--page);
  }
  .canvas {
    position: relative;
    width: 720px;
    height: 1200px;
  }
  .label {
    position: absolute;
    left: 30px;
    top: 435px;
    width: 660px;
    height: 330px;
    box-sizing: border-box;
    border: 1px solid var(--dieline);
    overflow: hidden;
    font-family: "Roboto", Arial, sans-serif;
    color: var(--ink);
  }
  .label__marble {
    position: absolute;
    inset: 0;
    background:
      radial-gradient(ellipse 55% 22% at 58% 36%, var(--marble-gold), transparent 70%),
      radial-gradient(ellipse 35% 30% at 85% 62%, var(--marble-gold), transparent 70%),
      linear-gradient(160deg, var(--marble-white) 0%, #fbf6ea 45%, var(--marble-white) 100%);
  }
  .ingredients, .producer {
    position: absolute;
    writing-mode: vertical-rl;
    transform: rotate(180deg);
    font-weight: 300;
    font-size: 11.2px;
    line-height: 16px;
    text-align: start;
    white-space: nowrap;
  }
  .ingredients {
    left: 12px;
    top: 30px;
    height: 278px;
  }
  .producer {
    left: 574px;
    top: 170px;
    height: 138px;
  }
  .producer .web { font-weight: 400; }
  .brand {
    position: absolute;
    left: 0;
    right: 0;
    top: 148px;
    text-align: center;
    font-weight: 300;
    font-size: 34px;
    letter-spacing: 2px;
    color: var(--ink);
  }
  .tagline {
    position: absolute;
    left: 0;
    right: 0;
    top: 208px;
    text-align: center;
    font-family: "Allura", cursive;
    font-size: 26px;
    color: var(--copper);
  }
  .claim {
    position: absolute;
    left: 206px;
    width: 246px;
    top: 264px;
    text-align: center;
    font-weight: 300;
    font-size: 15.5px;
    letter-spacing: -0.3px;
    color: var(--ink-soft);
    padding-bottom: 5px;
    border-bottom: 1px solid var(--ink-soft);
  }
  .volume {
    position: absolute;
    left: 0;
    right: 0;
    top: 297px;
    text-align: center;
    font-weight: 300;
    font-size: 10.5px;
    color: var(--ink-soft);
  }
  .gold-band {
    position: absolute;
    left: 0;
    right: 0;
    bottom: 0;
    height: 7px;
    background: linear-gradient(90deg, var(--gold-deep), var(--gold-mid) 35%, var(--gold-light) 55%, var(--gold-mid) 75%, var(--gold-deep));
  }
</style>
</head>
<body>
<main class="canvas">
  <section class="label">
    <div class="label__marble" role="img" aria-label="White marble background with flowing gold veins"></div>

    <p class="ingredients">A complex blend of Pure Oils including Marula,<br>Sea Buckthorn, Rosehip, Neroli, Evening primrose,<br>Argan, Calendula, Lavender, Jojoba, Grapeseed,<br>Baobab, Moringa and Vitamin E oil.</p>

    <h1 class="brand">Solvanta</h1>
    <p class="tagline">Regenerate , Hydrate , Glow</p>
    <p class="claim">%100 NATURAL &bull; LUXE FACIAL OIL</p>
    <p class="volume">1.01oz | 30ml</p>

    <p class="producer">Produced by Copper Lantern Ltd<br>P.O box 7825-00300<br>Nairobi, Kenya<br><span class="web">www.velmoraorganics.example</span></p>

    <div class="gold-band"></div>
  </section>
</main>
</body>
</html>
```